Finally a Vodka produced for women ! (Label Design)

We are a small distillery based in Melbourne, Australia and we need a Vodka label design solution that will appeal to women aged 30-50 years and radiate luxury. Full Details are in a design brief attached. We thank you in advance.

Target Market(s)

Affluent females 30-50 years.

Industry/Entity Type

Spirits/Alcohol

Requirements
Must have
• Be clear this is a luxury Vodka.
Nice to have
• Elegance.

```html
<!DOCTYPE html>
<html lang="en">
<head>
<meta charset="utf-8">
<title>Velvet Orla – Vodka Label Dielines</title>
<link rel="stylesheet" href="https://fonts.googleapis.com/css2?family=Barlow:wght@400;500&family=Barlow+Semi+Condensed:wght@400&display=swap">
<style>
  :root {
    --paper: #ffffff;
    --label-black: #000000;
    --pattern-grey: #262626;
    --brand-pink: #e0087e;
    --dieline-blue: #1a9ad6;
    --ink: #111111;
    --soft-white: #f2f2f2;
    --muted-grey: #9a9a9a;
    --band: #0b0b0b;
  }
  html, body {
    margin: 0;
    padding: 0;
    width: 849px;
    height: 1200px;
    overflow: hidden;
    background: var(--paper);
  }
  .sheet { display: block; width: 849px; height: 1200px; }
  .dimension-line { stroke: var(--dieline-blue); stroke-width: 1.3; fill: none; }
  .dimension-head { fill: var(--dieline-blue); }
  .dimension-text {
    font-family: "Barlow Semi Condensed", sans-serif;
    font-size: 24px;
    fill: var(--ink);
  }
  .cut-outline { fill: none; stroke: var(--dieline-blue); stroke-width: 1.4; }
  .brand-name {
    font-family: "Barlow", sans-serif;
    font-weight: 500;
    fill: var(--brand-pink);
    text-anchor: middle;
    letter-spacing: 0.04em;
  }
  .brand-name--neck { font-size: 34px; }
  .brand-name--body { font-size: 60px; }
  .product-type {
    font-family: "Barlow", sans-serif;
    font-size: 19px;
    letter-spacing: 0.22em;
    fill: var(--soft-white);
    text-anchor: middle;
  }
  .filter-band { fill: var(--band); }
  .filter-claim {
    font-family: "Barlow", sans-serif;
    font-size: 25px;
    letter-spacing: 0.08em;
    fill: var(--muted-grey);
    text-anchor: middle;
  }
  .abv {
    font-family: "Barlow", sans-serif;
    font-size: 16px;
    letter-spacing: 0.28em;
    fill: var(--soft-white);
    text-anchor: middle;
  }
</style>
</head>
<body>
<svg class="sheet" viewBox="0 0 849 1200" xmlns="http://www.w3.org/2000/svg">
  <defs>
    <linearGradient id="pattern-tone" x1="0" y1="0" x2="1" y2="1">
      <stop offset="0" stop-color="#1c1c1c"/>
      <stop offset="0.5" stop-color="#0a0a0a"/>
      <stop offset="1" stop-color="#1c1c1c"/>
    </linearGradient>
    <clipPath id="neck-clip"><rect x="219" y="131" width="396" height="197"/></clipPath>
  </defs>

  <!-- Neck label: width dimension -->
  <g class="neck-width">
    <text class="dimension-text" x="405" y="80" text-anchor="middle">100 mm</text>
    <line class="dimension-line" x1="212" y1="90" x2="611" y2="90"/>
    <path class="dimension-head" d="M211 90 L224 84 L220 90 L224 96 Z"/>
    <path class="dimension-head" d="M612 90 L599 84 L603 90 L599 96 Z"/>
  </g>

  <!-- Neck label -->
  <g class="neck-label">
    <rect x="219" y="131" width="396" height="197" fill="url(#pattern-tone)" role="img" aria-label="Dark grey lotus leaf pattern on black"/>
    <g clip-path="url(#neck-clip)">
      <text class="brand-name brand-name--neck" x="218" y="222">VELVET</text>
      <text class="brand-name brand-name--neck" x="218" y="272">ORLA</text>
      <text class="brand-name brand-name--neck" x="395" y="222">VELVET</text>
      <text class="brand-name brand-name--neck" x="395" y="272">ORLA</text>
      <text class="brand-name brand-name--neck" x="572" y="222">VELVET</text>
      <text class="brand-name brand-name--neck" x="572" y="272">ORLA</text>
    </g>
    <rect class="cut-outline" x="219" y="131" width="396" height="197"/>
  </g>

  <!-- Neck label: height dimension -->
  <g class="neck-height">
    <line class="dimension-line" x1="678" y1="132" x2="678" y2="328"/>
    <path class="dimension-head" d="M678 131 L672 144 L678 140 L684 144 Z"/>
    <path class="dimension-head" d="M678 329 L672 316 L678 320 L684 316 Z"/>
    <text class="dimension-text" x="705" y="231">50 mm</text>
  </g>

  <!-- Body label: width dimension -->
  <g class="body-width">
    <text class="dimension-text" x="405" y="444" text-anchor="middle">108.57 mm</text>
    <line class="dimension-line" x1="191" y1="440" x2="191" y2="912"/>
    <line class="dimension-line" x1="624" y1="440" x2="624" y2="912"/>
    <line class="dimension-line" x1="192" y1="468" x2="623" y2="468"/>
    <path class="dimension-head" d="M191 468 L204 462 L200 468 L204 474 Z"/>
    <path class="dimension-head" d="M624 468 L611 462 L615 468 L611 474 Z"/>
  </g>

  <!-- Body label -->
  <g class="body-label">
    <polygon points="312,545 411,586 504,545 638,886 435,1019 380,1019 177,886"
             fill="url(#pattern-tone)" stroke="var(--label-black)" stroke-width="6" stroke-linejoin="round"
             role="img" aria-label="Dark grey lotus leaf pattern on black"/>
    <text class="brand-name brand-name--body" x="408" y="712">VELVET</text>
    <text class="brand-name brand-name--body" x="408" y="800">ORLA</text>
    <text class="product-type" x="408" y="846">PREMIUM VODKA</text>
    <rect class="filter-band" x="254" y="873" width="308" height="35"/>
    <text class="filter-claim" x="408" y="900">ROSE QUARTZ FILTERED</text>
    <text class="abv" x="406" y="962">40% ALC/VOL</text>
    <polygon class="cut-outline" points="318,561 411,599 497,561 624,882 432,1006 383,1006 191,882"/>
  </g>

  <!-- Body label: height dimension -->
  <g class="body-height">
    <line class="dimension-line" x1="524" y1="559" x2="745" y2="559"/>
    <line class="dimension-line" x1="453" y1="1006" x2="745" y2="1006"/>
    <line class="dimension-line" x1="703" y1="560" x2="703" y2="1005"/>
    <path class="dimension-head" d="M703 559 L697 572 L703 568 L709 572 Z"/>
    <path class="dimension-head" d="M703 1006 L697 993 L703 997 L709 993 Z"/>
    <text class="dimension-text" x="713" y="796">112.06 mm</text>
  </g>
</svg>
</body>
</html>
```